INSURANCE COMPANY POSTCARD

WE ARE A WELL KNOWN INSURANCE AGENCY WORKING UNDER NEW OWNERSHIP USING THE OLD OWNERS NAME STILL, AS OUR TINY COMMUNITY WOULDN'T BE ABLE TO UNDERSTAND THAT WE ARE THE SAME AS BEFORE, JUST A NEW OWNER. WE PROVIDE AUTO, HOME, COMMERCIAL, FLOOD AND EVENT INSURANCE.

Industry/Entity Type

Insurance

```html
<!DOCTYPE html>
<html lang="en">
<head>
<meta charset="utf-8">
<title>Hale Insurance Agency – Postcard</title>
<link href="https://fonts.googleapis.com/css2?family=Cinzel:wght@400;700&family=Oswald:wght@500&family=Open+Sans:wght@400&display=swap" rel="stylesheet">
<style>
  :root {
    --navy: #0d1d3d;
    --blue: #2f7ec1;
    --orange: #f4a11d;
    --white: #ffffff;
    --stage: #ababab;
    --icon-blue: #3c86cc;
    --faint: #e2e4e8;
  }
  * { box-sizing: border-box; margin: 0; padding: 0; }
  html, body { width: 1200px; height: 720px; overflow: hidden; }
  body { background: var(--stage); position: relative; font-family: "Open Sans", sans-serif; }

  .card { position: absolute; background: var(--white); overflow: hidden; box-shadow: 4px 6px 10px rgba(0,0,0,0.35); }
  .card--front { left: 70px; top: 228px; width: 480px; height: 370px; }
  .card--back { left: 600px; top: 91px; width: 478px; height: 368px; }

  .brand-name { font-family: "Cinzel", serif; font-weight: 700; text-align: center; line-height: 1; display: block; }

  /* Front */
  .front-photo {
    position: absolute; inset: 0;
    background: linear-gradient(120deg, #c9d5e6 0%, #eef1f6 35%, #dfe6ef 55%, #8fa3c0 80%, #56698c 100%);
  }
  .front-edge { position: absolute; left: 0; top: 0; width: 16px; height: 230px; background: var(--white); }
  .front-brand-panel {
    position: absolute; left: 16px; top: 0; width: 181px; height: 230px;
    background: var(--navy);
    display: flex; flex-direction: column; align-items: center; justify-content: center; gap: 16px;
  }
  .panel-circle { width: 92px; height: 92px; border: 3px solid var(--white); border-radius: 50%; }
  .front-brand-panel .brand-name { color: var(--white); font-size: 36px; letter-spacing: 2px; }
  .front-accent { position: absolute; left: 0; top: 230px; width: 16px; height: 54px; background: var(--orange); }
  .front-edge-low { position: absolute; left: 0; top: 284px; width: 16px; height: 86px; background: var(--white); }
  .coverage-band {
    position: absolute; left: 197px; top: 230px; width: 283px; height: 54px;
    background: var(--navy);
    display: flex; align-items: center; justify-content: center; gap: 9px;
    font-family: "Oswald", sans-serif; font-weight: 500; font-size: 14px;
    color: var(--orange); letter-spacing: 0.2px;
  }
  .brand-box {
    position: absolute; left: 16px; top: 284px; width: 181px; height: 86px;
    background: var(--white);
    display: flex; flex-direction: column; align-items: center; justify-content: center;
  }
  .brand-box .brand-name { color: var(--navy); }
  .brand-box .brand-name--main { font-size: 50px; letter-spacing: 2px; }
  .brand-box .brand-name--sub { font-size: 11px; letter-spacing: 1.2px; margin-top: 4px; }

  /* Back */
  .headline-box {
    position: absolute; left: 0; top: 0; width: 286px; height: 113px;
    background: var(--blue); color: var(--white);
    font-family: "Cinzel", serif; font-weight: 400; font-size: 25px; line-height: 1.2;
    padding: 26px 0 0 12px;
  }
  .headline-box .line-two { display: block; padding-left: 37px; }
  .back-block-navy { position: absolute; left: 288px; top: 0; width: 55px; height: 113px; background: var(--navy); }
  .icon-strip {
    position: absolute; left: 0; top: 115px; width: 286px; height: 53px;
    background: var(--navy);
    display: flex; align-items: center; justify-content: space-around; padding: 0 6px;
  }
  .icon-strip svg { width: 30px; height: 26px; fill: none; stroke: var(--icon-blue); stroke-width: 2; }
  .icon-strip svg .solid { fill: var(--icon-blue); stroke: none; }
  .back-block-orange { position: absolute; left: 288px; top: 115px; width: 55px; height: 53px; background: var(--orange); }
  .faint-mark {
    position: absolute; left: 343px; top: 20px; width: 135px; height: 260px;
    display: flex; flex-direction: column; align-items: center; justify-content: center; gap: 14px;
  }
  .faint-circle { width: 90px; height: 90px; border: 4px solid var(--faint); border-radius: 50%; }
  .faint-mark .brand-name { color: var(--faint); font-size: 36px; letter-spacing: 1px; }
  .contact-lines {
    position: absolute; left: 12px; top: 262px;
    font-family: "Cinzel", serif; font-weight: 700; font-size: 12px; color: var(--navy); line-height: 1.35;
  }
  .contact-rule { position: absolute; left: 0; top: 302px; width: 286px; height: 1px; background: var(--blue); }
  .staff-list {
    position: absolute; left: 12px; top: 310px; list-style: none;
    font-size: 9.5px; color: var(--navy); line-height: 1.5;
  }
  .back-brand {
    position: absolute; right: 26px; top: 303px;
    display: flex; flex-direction: column; align-items: center;
  }
  .back-brand .brand-name { color: var(--navy); }
  .back-brand .brand-name--main { font-size: 42px; letter-spacing: 2px; }
  .back-brand .brand-name--sub { font-size: 9px; letter-spacing: 1px; margin-top: 3px; }
</style>
</head>
<body>

<section class="card card--front" aria-label="Postcard front">
  <div class="front-photo" role="img" aria-label="Soft-focus photo of a hand holding a pen over financial charts and paperwork"></div>
  <div class="front-edge"></div>
  <div class="front-brand-panel">
    <span class="panel-circle" aria-hidden="true"></span>
    <span class="brand-name">HALE</span>
  </div>
  <div class="front-accent"></div>
  <div class="front-edge-low"></div>
  <div class="coverage-band">
    <span>AUTO</span><span>HOME</span><span>COMMERCIAL</span><span>FLOOD</span><span>EVENT</span>
  </div>
  <div class="brand-box">
    <span class="brand-name brand-name--main">HALE</span>
    <span class="brand-name brand-name--sub">INSURANCE AGENCY</span>
  </div>
</section>

<section class="card card--back" aria-label="Postcard back">
  <div class="faint-mark" aria-hidden="true">
    <span class="faint-circle"></span>
    <span class="brand-name">HALE</span>
  </div>
  <h1 class="headline-box">We are the same <span class="line-two">with New Face</span></h1>
  <div class="back-block-navy"></div>
  <div class="icon-strip">
    <svg viewBox="0 0 32 28" aria-label="Auto"><path class="solid" d="M3 18 L6 11 Q7 9 10 9 L22 9 Q25 9 26 11 L29 18 L29 22 L3 22 Z"/><circle class="solid" cx="9" cy="23" r="3"/><circle class="solid" cx="23" cy="23" r="3"/></svg>
    <svg viewBox="0 0 32 28" aria-label="Home"><path class="solid" d="M16 3 L29 14 L25 14 L25 25 L19 25 L19 18 L13 18 L13 25 L7 25 L7 14 L3 14 Z"/></svg>
    <svg viewBox="0 0 32 28" aria-label="Commercial"><path d="M8 26 L8 8 L16 4 L16 26 M16 10 L24 10 L24 26 M5 26 L27 26 M11 12 L13 12 M11 17 L13 17 M11 22 L13 22 M19 15 L21 15 M19 20 L21 20"/></svg>
    <svg viewBox="0 0 32 28" aria-label="Flood"><path d="M3 9 Q7 5 11 9 T19 9 T29 9 M3 15 Q7 11 11 15 T19 15 T29 15 M3 21 Q7 17 11 21 T19 21 T29 21"/></svg>
    <svg viewBox="0 0 32 28" aria-label="Event"><rect x="5" y="5" width="22" height="20" rx="2"/><path d="M5 10 L27 10 M10 2 L10 7 M22 2 L22 7"/><path d="M9 14 h2 M15 14 h2 M21 14 h2 M9 19 h2 M15 19 h2 M21 19 h2"/></svg>
  </div>
  <div class="back-block-orange"></div>

  <p class="contact-lines">Phone : 318-555-0142<br>Fax : 318-555-0143</p>
  <div class="contact-rule"></div>
  <ul class="staff-list">
    <li>mreedhale@mail.net mara reed - owner/sales/agent</li>
    <li>jpaxhale@mail.net jo paxton - agent</li>
    <li>tlanehale@mail.com tess lane - csr/agent</li>
  </ul>

  <div class="back-brand">
    <span class="brand-name brand-name--main">HALE</span>
    <span class="brand-name brand-name--sub">INSURANCE AGENCY</span>
  </div>
</section>

</body>
</html>
```